Sales Website Design

Create a sales-oriented website to advertise turn-key solutions for providing infection control to senior housing operators. There are several items uploaded. The pdf should serve as your guide. The powerpoint presentation has additional information.

The idea is this is senior housing reimagined for infection control. The design should be sleek, clean, vibrant and energetic.

Our goal is to sell a turnkey solution for making buildings safer for residents, staff, and families.

Target Market(s)

People who own and operate senior housing communities

Coding

Coded - Design and coding required

Number of Pages Required

5+ page

```html
<!DOCTYPE html>
<html lang="en">
<head>
<meta charset="utf-8">
<title>Clear Harbor – Senior Living Communities</title>
<link rel="stylesheet" href="https://fonts.googleapis.com/css2?family=Rajdhani:wght@500;600;700&family=Raleway:wght@400;500;600&display=swap">
<style>
:root{
  --orange:#e8411e;
  --navy:#13242c;
  --ink:#1d2b33;
  --text:#6b6b6b;
  --line:#dcdcdc;
  --footer:#202020;
  --white:#ffffff;
}
*{box-sizing:border-box;margin:0;padding:0}
html,body{width:1200px;height:3912px;overflow:hidden;background:var(--white)}
body{position:relative;font-family:"Raleway",Arial,sans-serif;color:var(--ink)}
.abs{position:absolute}
.display{font-family:"Rajdhani",Arial,sans-serif;font-weight:700;text-transform:uppercase;letter-spacing:.5px}
.accent{color:var(--orange)}
.btn{position:absolute;background:var(--orange);color:var(--white);font-family:"Rajdhani",sans-serif;font-weight:600;font-size:16px;display:flex;align-items:center;justify-content:center;letter-spacing:.5px;text-transform:uppercase}

/* header */
.brand{left:111px;top:16px;font-size:34px;color:var(--orange)}
.topbar{right:112px;top:22px;display:flex;align-items:center;gap:10px;font-size:15px}
.topbar .call{color:var(--orange);font-family:"Rajdhani",sans-serif;font-weight:600;font-size:16px}
.topbar .num{font-family:"Rajdhani",sans-serif;font-size:23px;font-weight:500;margin-right:18px}
.topbar .login{font-family:"Rajdhani",sans-serif;font-weight:600;font-size:15px;color:#333;margin-right:14px}
.nav{left:111px;top:71px;width:977px;height:73px;background:var(--navy);display:flex;align-items:center;justify-content:space-around;padding:0 30px;z-index:2}
.nav a{color:var(--white);text-decoration:none;font-family:"Rajdhani",sans-serif;font-weight:500;font-size:16px;letter-spacing:.5px}
.nav a.current{color:var(--orange)}

/* hero */
.hero{left:0;top:103px;width:1200px;height:558px;background:linear-gradient(180deg,#5a6b4b 0%,#4c5d45 40%,#3e4d3c 100%)}
.hero-title{left:0;top:288px;width:1200px;text-align:center;color:var(--white);font-size:76px;line-height:1}
.hero-sub{left:0;top:364px;width:1200px;text-align:center;color:var(--white);font-size:25px}
.dots{left:554px;top:629px;display:flex;gap:12px}
.dots span{width:14px;height:14px;border:2px solid var(--white);border-radius:50%}
.dots span.on{background:var(--white)}

/* benefits */
.sketch{left:955px;top:661px;width:245px;height:524px;background:linear-gradient(90deg,rgba(255,255,255,0),rgba(220,224,228,.55))}
.section-title{left:0;width:1200px;text-align:center;font-size:42px;line-height:1}
.card{top:825px;width:238px;height:258px;background:var(--white);border:1px solid #e3e3e3;border-radius:8px;box-shadow:0 2px 8px rgba(0,0,0,.1);display:flex;flex-direction:column;align-items:center;justify-content:center;gap:28px}
.card .icon{width:86px;height:86px;border-radius:6px;background:rgba(232,65,30,.12);border:2px solid var(--orange)}
.card h3{font-family:"Rajdhani",sans-serif;font-weight:700;font-size:19px;letter-spacing:.5px}
.card.feature{background:linear-gradient(180deg,#3a2c28,#171312);border:none;gap:10px;padding:0 18px;color:var(--white);text-align:center}
.card.feature .icon{width:60px;height:60px}
.card.feature p{font-size:12.5px;line-height:26px}

/* products */
.products{left:0;top:1185px;width:1200px;height:513px;background:var(--navy)}
.products-title{top:1262px;color:var(--white);font-weight:500;font-size:48px}
.rule{left:570px;top:1320px;width:60px;height:3px;background:var(--white)}
.lead{left:140px;top:1344px;width:920px;text-align:center;color:#e9ecee;font-size:18px;line-height:29px}
.bubble{top:1445px;width:170px;height:170px;border-radius:50%;display:flex;align-items:center;justify-content:center;text-align:center;font-family:"Rajdhani",sans-serif;font-size:22px;font-weight:500;line-height:28px}
.bubble.solid{background:var(--orange);color:var(--white);box-shadow:0 0 0 5px var(--navy),0 0 0 8px #243a44}
.bubble.ring{background:var(--white);color:var(--ink);border:8px solid var(--orange)}

/* in action */
.action-title{left:111px;top:1830px;font-size:42px;line-height:1}
.action-text{left:111px;top:1886px;width:460px;color:var(--text);font-size:15.5px;line-height:34.5px;text-align:justify}
.action-photo{left:592px;top:1803px;width:496px;height:390px;background:linear-gradient(135deg,#e6e7ea,#cfd1d4 55%,#b9aa92);box-shadow:0 2px 6px rgba(0,0,0,.2)}

/* marketing */
.marketing{left:0;top:2297px;width:1200px;height:513px;background:linear-gradient(180deg,#26302c,#1c2422)}
.marketing-title{left:0;top:2420px;width:1200px;text-align:center;color:var(--white);font-size:42px;line-height:1}
.marketing-text{left:110px;top:2478px;width:980px;text-align:center;color:var(--white);font-size:15.5px;line-height:34.5px}

/* contact */
.contact-title{top:2910px}
.field{position:absolute;border:1px solid var(--line);box-shadow:0 1px 4px rgba(0,0,0,.08);background:var(--white);font-size:16px;color:#444;padding:0 12px;display:flex;align-items:center}
.field.area{align-items:flex-start;padding-top:28px}
.forgot{left:146px;top:3434px;font-size:16px;color:#444}
.submit{font-size:21px;font-weight:700}
.sketch-left{left:0;top:3160px;width:300px;height:417px;background:linear-gradient(90deg,rgba(220,224,228,.5),rgba(255,255,255,0))}

/* footer */
.footer{left:0;top:3577px;width:1200px;height:335px;background:var(--footer)}
.footer-brand{left:110px;top:3685px;font-family:"Rajdhani",sans-serif;font-weight:500;font-size:52px;color:var(--white)}
.col-title{top:3630px;color:var(--white);font-family:"Rajdhani",sans-serif;font-weight:700;font-size:15px;letter-spacing:.5px}
.menu{left:520px;top:3666px;list-style:none;color:#ddd;font-size:13px;line-height:21.5px;text-transform:uppercase}
.info{display:flex;gap:14px;color:#ddd;font-size:12.5px;line-height:16px;align-items:center}
.info .dot{width:26px;height:26px;border-radius:50%;background:var(--white);flex:none;display:flex;align-items:center;justify-content:center}
.footer-rule{left:92px;top:3851px;width:1016px;height:1px;background:#3a3a3a}
.copyright{left:0;top:3872px;width:1200px;text-align:center;color:#ccc;font-size:10.5px}
</style>
</head>
<body>

<!-- header -->
<div class="abs display brand">Clear Harbor</div>
<div class="abs topbar">
  <svg width="18" height="18" viewBox="0 0 18 18"><rect width="18" height="18" rx="3" fill="#e8411e"/><path d="M5 4.5l2 -.3 1 2.3-1.2 1a6 6 0 0 0 3 3l1-1.2 2.3 1-.3 2c-4 .4-8.2-3.8-7.8-7.8z" fill="#fff"/></svg>
  <span class="call">CALL NOW -</span><span class="num">555-010-2040</span>
  <svg width="16" height="18" viewBox="0 0 16 18" fill="none" stroke="#e8411e" stroke-width="1.6"><circle cx="8" cy="5" r="4"/><path d="M1 17c0-4 3-6 7-6s7 2 7 6z"/></svg>
  <span class="login">LOG IN</span>
  <svg width="15" height="15" viewBox="0 0 15 15" fill="none" stroke="#222" stroke-width="2"><circle cx="6" cy="6" r="4.5"/><path d="M9.5 9.5l4 4"/></svg>
</div>
<nav class="abs nav">
  <a class="current" href="#">HOME</a><a href="#">PRODUCTS</a><a href="#">TECHNOLOGY</a><a href="#">BENEFITS</a><a href="#">MARKETING</a><a href="#">PROCESS</a><a href="#">CASE STUDY</a><a href="#">CONTACT</a>
</nav>

<!-- hero -->
<div class="abs hero" role="img" aria-label="Aerial view of a leafy residential neighbourhood"></div>
<h1 class="abs display hero-title">Clear Harbor</h1>
<p class="abs hero-sub">Senior Living Communities Centered on Safety &amp; Efficiency</p>
<div class="btn" style="left:539px;top:415px;width:155px;height:51px">Get Started</div>
<div class="abs dots"><span class="on"></span><span></span><span></span><span></span></div>

<!-- benefits -->
<div class="abs sketch" role="img" aria-label="Faint architectural line sketch of a building"></div>
<h2 class="abs display section-title" style="top:758px"><span class="accent">Clear Harbor</span> Benefits</h2>
<div class="abs card" style="left:111px"><div class="icon" role="img" aria-label="Residents icon"></div><h3>RESIDENTS</h3></div>
<div class="abs card feature" style="left:358px"><div class="icon" role="img" aria-label="Family icon"></div><h3>FAMILY &amp; FRIENDS</h3><p>Reduce feelings of guilt when a loved one chooses a senior living setting Convenience ( virtual "shopping" platform ) Promote safe &amp; healthy visits</p></div>
<div class="abs card" style="left:605px"><div class="icon" role="img" aria-label="Staff icon"></div><h3>STAFF</h3></div>
<div class="abs card" style="left:849px"><div class="icon" role="img" aria-label="Owners icon"></div><h3>OWNERS</h3></div>

<!-- products -->
<section class="abs products"></section>
<h2 class="abs display section-title products-title">Products and Technology</h2>
<div class="abs rule"></div>
<p class="abs lead">Senior housing has an extraordinary opportunity to embrace technological advances that will simultaneously increase operational efficiencies and improve resident health outcomes</p>
<div class="abs bubble solid" style="left:143px">Touchless<br>Temperature<br>Scans</div>
<div class="abs bubble ring" style="left:328px">Wireless<br>Diagnostic<br>equipment</div>
<div class="abs bubble solid" style="left:515px">Wearable<br>Monitoring</div>
<div class="abs bubble ring" style="left:700px">Wearable<br>Monitoring</div>
<div class="abs bubble solid" style="left:887px">UV<br>Sanitation<br>Devices</div>

<!-- in action -->
<h2 class="abs display action-title"><span class="accent">Clear Harbor</span> In Action</h2>
<p class="abs action-text">Nemo enim ipsam voluptatem quia voluptas sit aspernatur aut odit aut fugit, sed quia consequuntur magni dolores eos qui ratione voluptatem sequi nesciunt. Neque porro quisquam est, qui dolorem ipsum quia dolor sit amet, consectetur, adipisci velit, sed quia non numquam eius modi tempora incidunt ut labore et dolore magnam aliquam quaerat voluptatem</p>
<div class="btn" style="left:111px;top:2108px;width:155px;height:51px">Read More</div>
<div class="abs action-photo" role="img" aria-label="Tablet showing a bathroom interior on top of floor plans with drafting tools"></div>

<!-- marketing -->
<section class="abs marketing" role="img" aria-label="Dimmed aerial view of a residential neighbourhood"></section>
<h2 class="abs display marketing-title">Marketing</h2>
<p class="abs marketing-text">Nemo enim ipsam voluptatem quia voluptas sit aspernatur aut odit aut fugit, sed quia consequuntur magni dolores eos qui ratione voluptatem sequi nesciunt. Neque porro quisquam est, qui dolorem ipsum quia dolor sit amet, consectetur, adipisci velit, sed quia non numquam eius modi tempora incidunt ut labore et dolore magnam aliquam quaerat voluptatem. Ut enim ad minima veniam, quis nostrum exercitationem ullam corporis suscipit laboriosam, nisi ut aliquid ex ea commodi consequatur</p>
<div class="btn" style="left:523px;top:2629px;width:154px;height:51px">Contact Us</div>

<!-- contact -->
<div class="abs sketch-left" role="img" aria-label="Faint architectural line sketch of a tower"></div>
<h2 class="abs display section-title contact-title">Contact Us</h2>
<div class="field" style="left:137px;top:2974px;width:454px;height:64px">First Name</div>
<div class="field" style="left:608px;top:2974px;width:455px;height:64px">Last Name</div>
<div class="field" style="left:137px;top:3052px;width:454px;height:63px">Phone</div>
<div class="field" style="left:608px;top:3052px;width:455px;height:63px">Email</div>
<div class="field" style="left:137px;top:3134px;width:926px;height:64px">Business</div>
<div class="field area" style="left:137px;top:3213px;width:926px;height:176px">Type here</div>
<p class="abs forgot">Forgot password?</p>
<div class="btn submit" style="left:608px;top:3415px;width:455px;height:61px">SUBMIT</div>

<!-- footer -->
<footer class="abs footer"></footer>
<div class="abs footer-brand">Clear Harbor</div>
<div class="abs col-title" style="left:520px">MENU</div>
<ul class="abs menu"><li>Products</li><li>Technology</li><li>Benefits</li><li>Marketing</li><li>Process</li><li>Case Study</li><li>Contact</li></ul>
<div class="abs col-title" style="left:697px">CONTACT US</div>
<div class="abs info" style="left:695px;top:3670px"><span class="dot"><svg width="10" height="13" viewBox="0 0 10 13"><path d="M5 0a5 5 0 0 1 5 5c0 3-5 8-5 8S0 8 0 5a5 5 0 0 1 5-5z" fill="#202020"/><circle cx="5" cy="5" r="1.8" fill="#fff"/></svg></span><span>410 Maple Ridge Lane,<br>Lakeview B.C.</span></div>
<div class="abs info" style="left:695px;top:3725px"><span class="dot"><svg width="11" height="11" viewBox="0 0 18 18"><path d="M3 1l4-.5 2 4.5-2.4 2a11 11 0 0 0 5 5l2-2.4 4.5 2-.5 4C9 17 1 9 3 1z" fill="#202020"/></svg></span><span>Call Us<br>555.010.2040</span></div>
<div class="abs info" style="left:695px;top:3780px"><span class="dot"><svg width="12" height="9" viewBox="0 0 12 9"><rect width="12" height="9" rx="1" fill="#202020"/><path d="M0 1l6 4 6-4" stroke="#fff" fill="none"/></svg></span><span>E mail Us<br>info@clearharbor.example</span></div>
<div class="abs col-title" style="left:978px">FOLLOW US</div>
<div class="abs info" style="left:977px;top:3670px"><span class="dot"></span><span>Like us on<br>SOCIAL PAGE</span></div>
<div class="abs info" style="left:977px;top:3725px"><span class="dot"></span><span>Follow us on<br>NEWS FEED</span></div>
<div class="abs info" style="left:977px;top:3780px"><span class="dot"></span><span>Follow us on<br>PRO NETWORK</span></div>
<div class="abs footer-rule"></div>
<p class="abs copyright">Copyright © 2020 All Rights Reserved</p>

</body>
</html>
```